Domestic Building Company requires professional webpage

We have an existing webpage that was never completed. We are a growing building company specialising in domestic building, renovations and commercial maintenance. We liaise closely with each of our clients to provide quality service they would be happy to recommend. Our easy approachable staff give our clients the confidence to discuss their needs and changes they may have along the way.
Our main source of new customers have been from recommendations of existing clients.
We would like our webpage to reflect our eye for detail and showcase our previous work.
The colour theme should be the same as the colours of our logo.
We would like the main page to really stand out with a slideshow of our pictures of works we have completed.
We would like the tabs to remain the same - Home, About Us, Our Services, Contact us.
In the Our Services section we would like each sub heading to be a link where viewers can see pictures from previous work we have completed.
Our current web page is www.ferncastconstruct.com.au

```html
<!DOCTYPE html>
<html lang="en">
<head>
<meta charset="utf-8">
<title>Ferncast Construct Pty Ltd</title>
<link href="https://fonts.googleapis.com/css2?family=Montserrat:wght@300;400;700&family=Play&family=Arimo:wght@400&display=swap" rel="stylesheet">
<style>
:root{
  --blue:#0467b8;
  --green:#7cc35b;
  --green-soft:#c5e2bb;
  --ink:#1c1c1c;
  --text:#3b3b3b;
  --page:#ebebeb;
  --footer:#282828;
  --footer-line:#444;
  --bar:#3a3a3a;
}
*{margin:0;padding:0;box-sizing:border-box}
html,body{width:1120px;height:1200px;overflow:hidden}
body{position:relative;background:var(--page);font-family:"Montserrat",sans-serif;color:var(--text)}
.site-header{position:absolute;left:0;top:0;width:1120px;height:114px;background:linear-gradient(#ececec,#fafafa 60%,#fff)}
.brand{position:absolute;left:143px;top:30px;display:flex;align-items:center;gap:12px}
.brand-mark{width:52px;height:52px;background:var(--blue)}
.brand-name{font-family:"Montserrat",sans-serif;font-weight:400;font-size:30px;color:var(--blue);line-height:1}
.header-contact{position:absolute;right:126px;top:34px;text-align:right;color:var(--green)}
.header-phone{font-family:"Play",sans-serif;font-size:30px;line-height:1;display:flex;align-items:center;justify-content:flex-end;gap:6px}
.header-email{font-family:"Arimo",sans-serif;font-size:16px;margin-top:9px;display:flex;align-items:center;justify-content:flex-end;gap:6px}
.main-nav{position:absolute;left:0;top:114px;width:1120px;height:35px;background:var(--blue);display:flex;padding-left:153px;gap:0}
.main-nav a{font-family:"Play",sans-serif;color:#fff;text-decoration:none;font-size:17px;line-height:35px;margin-right:44px}
.hero{position:absolute;left:0;top:149px;width:1120px;height:319px;background:linear-gradient(90deg,#7e7a68,#a9a792 50%,#6f7761)}
.hero-slide{position:absolute;left:127px;top:0;width:866px;height:319px;background:linear-gradient(160deg,#b59a74 0%,#6e5e4e 45%,#4d4a48 75%,#9a8a78 100%)}
.hero-dots{position:absolute;left:394px;top:295px;display:flex;gap:5px}
.hero-dots span{width:15px;height:14px;background:#fff;border:1px solid #ccc}
.hero-dots span.active{background:#b1302b}
.services-band{position:absolute;left:0;top:468px;width:1120px;height:120px;background:linear-gradient(var(--green-soft),var(--page))}
.section-title{position:absolute;font-family:"Montserrat",sans-serif;font-weight:700;color:var(--ink);letter-spacing:.5px}
.services-title{left:127px;top:485px;font-size:19px}
.service-grid{position:absolute;left:127px;top:518px;display:grid;grid-template-columns:repeat(4,204px);column-gap:16px;row-gap:16px}
.service-tile{position:relative;height:114px;display:block;text-decoration:none}
.service-tile .caption{position:absolute;left:0;bottom:0;width:100%;height:38px;background:rgba(30,30,30,.82);color:#fff;font-family:"Arimo",sans-serif;font-size:11.5px;line-height:13px;display:flex;align-items:center;padding:0 5px}
.welcome-title{left:127px;top:796px;font-size:19px}
.welcome-text{position:absolute;left:127px;top:830px;width:612px;font-size:10.8px;line-height:16px;font-weight:400}
.welcome-divider{position:absolute;left:779px;top:834px;width:1px;height:84px;background:#bbb}
.badge{position:absolute;left:823px;top:834px;width:169px;height:79px;background:#fff;border:1px solid var(--blue)}
.site-footer{position:absolute;left:0;top:986px;width:1120px;height:189px;background:var(--footer)}
.footer-heading{position:absolute;top:20px;font-family:"Arimo",sans-serif;color:var(--green);font-size:18px}
.footer-links{position:absolute;left:144px;top:52px;list-style:none}
.footer-links li{font-family:"Arimo",sans-serif;color:#fff;font-size:11.5px;line-height:24.5px}
.footer-divider{position:absolute;top:56px;width:1px;height:116px;background:var(--footer-line)}
.contact-row{position:absolute;left:384px;display:flex;align-items:flex-start;gap:10px;color:#eee;font-size:10.5px;line-height:13px}
.contact-row svg{flex:none}
.socials{position:absolute;left:386px;top:148px;display:flex;gap:9px}
.socials span{width:31px;height:31px;border-radius:50%;background:#555;border:2px solid #777}
.field{position:absolute;border:1px solid #555;background:#262626;color:#aaa;font-size:10.5px;padding:3px 9px;font-family:"Montserrat",sans-serif}
.send{position:absolute;left:815px;top:144px;width:119px;height:21px;background:var(--green);color:#fff;font-size:11px;text-align:center;line-height:21px;font-family:"Montserrat",sans-serif}
.copyright{position:absolute;left:0;top:1175px;width:1120px;height:25px;background:var(--bar);color:#aaa;font-size:10.5px;text-align:center;line-height:25px}
</style>
</head>
<body>
<header class="site-header">
  <div class="brand"><span class="brand-name">ferncast construct</span><span class="brand-mark"></span></div>
  <div class="header-contact">
    <div class="header-phone">
      <svg width="12" height="18" viewBox="0 0 12 18"><rect x="1" y="1" width="10" height="16" rx="2" fill="none" stroke="currentColor" stroke-width="2"/><circle cx="6" cy="14" r="1.2" fill="currentColor"/></svg>
      0400 555 182</div>
    <div class="header-email">
      <svg width="18" height="13" viewBox="0 0 18 13"><rect width="18" height="13" fill="currentColor"/><path d="M0 0l9 7 9-7" fill="none" stroke="#fff" stroke-width="1.5"/></svg>
      info@ferncastconstruct.com.au</div>
  </div>
</header>
<nav class="main-nav"><a href="#">Home</a><a href="#">About Us</a><a href="#">Our Services</a><a href="#">Contact Us</a></nav>

<section class="hero">
  <div class="hero-slide" role="img" aria-label="Photo of a completed open-plan living room renovation with timber floors and grey sofa">
    <div class="hero-dots"><span class="active"></span><span></span><span></span><span></span></div>
  </div>
</section>

<div class="services-band"></div>
<h2 class="section-title services-title">Our Services</h2>
<div class="service-grid">
  <a class="service-tile" href="#" role="img" aria-label="Photo of a residential house extension" style="background:linear-gradient(#5b6a4e,#8d8a70)"><span class="caption">RESIDENTIAL HOUSE EXTENSIONS<br>AND RENOVATIONS</span></a>
  <a class="service-tile" href="#" role="img" aria-label="Photo of a timber pergola in a garden" style="background:linear-gradient(#9fa595,#6e5a46)"><span class="caption">&nbsp;PERGOLAS</span></a>
  <a class="service-tile" href="#" role="img" aria-label="Photo of a timber deck with glass balustrade" style="background:linear-gradient(#7f7f7a,#4c4a46)"><span class="caption">&nbsp;DECKS</span></a>
  <a class="service-tile" href="#" role="img" aria-label="Photo of a renovated bathroom vanity" style="background:linear-gradient(#f1f1f1,#a9a49d)"><span class="caption">BATHROOMS</span></a>
  <a class="service-tile" href="#" role="img" aria-label="Photo of a commercial office fit-out" style="background:linear-gradient(#8c6b4e,#d6d2cc)"><span class="caption">COMMERCIAL FIT-OUT</span></a>
  <a class="service-tile" href="#" role="img" aria-label="Photo of timber flooring" style="background:linear-gradient(#7b746c,#4f4a44)"><span class="caption">TIMBER FLOORING</span></a>
  <a class="service-tile" href="#" role="img" aria-label="Photo of aluminium and timber slat screening" style="background:linear-gradient(90deg,#cfd0c8,#8a5a3c)"><span class="caption">&nbsp;ALUMINIUM / TIMBER</span></a>
  <a class="service-tile" href="#" role="img" aria-label="Photo of tiled floor maintenance work" style="background:linear-gradient(#7c848a,#4c5358)"><span class="caption">&nbsp;BUILDING MAINTENANCE</span></a>
</div>

<h2 class="section-title welcome-title">Welcome to Ferncast Construct Pty Ltd</h2>
<p class="welcome-text">Ferncast Construct Pty Ltd is a construction and renovation company that is based in the Illawarra area.&nbsp; We specialise in all areas of residential and commercial building works and aim to deliver the highest quality performance at an affordable price. We ensure our workers have undergone the qualifications and training to provide the workmanship, efficiency and reliability our clients expect. We actively engage our client from the initial greeting to the finished product, we achieve this by ensuring the clients needs remain our first priority when delivering a high quality service and product.</p>
<div class="welcome-divider"></div>
<div class="badge" role="img" aria-label="Industry association membership badge"></div>

<footer class="site-footer">
  <h3 class="footer-heading" style="left:141px">Site map</h3>
  <ul class="footer-links"><li>Home</li><li>About Us</li><li>Our Services</li><li>Contact us</li></ul>
  <div class="footer-divider" style="left:298px"></div>
  <h3 class="footer-heading" style="left:383px">Contact info</h3>
  <div class="contact-row" style="top:55px">
    <svg width="12" height="17" viewBox="0 0 12 17"><path d="M6 1a5 5 0 0 0-5 5c0 4 5 10 5 10s5-6 5-10a5 5 0 0 0-5-5z" fill="none" stroke="#999" stroke-width="1.5"/><circle cx="6" cy="6" r="1.8" fill="#999"/></svg>
    <span>Lorem Ipsum. Proin gravida nibh<br>vel velit auctor aliquet. Aenean</span></div>
  <div class="contact-row" style="top:97px">
    <svg width="13" height="11" viewBox="0 0 13 11"><path d="M1 3c3-3 8-3 11 0v2H9V3.5H4V5H1z M3 6h7l1 4H2z" fill="#999"/></svg>
    <span>0400 555 182</span></div>
  <div class="contact-row" style="top:121px">
    <svg width="13" height="11" viewBox="0 0 13 11"><rect width="13" height="11" fill="#999"/><path d="M0 0l6.5 5 6.5-5" fill="none" stroke="#282828" stroke-width="1.2"/></svg>
    <span>info@ferncastconstruct.com.au</span></div>
  <div class="socials"><span></span><span></span><span></span></div>
  <div class="footer-divider" style="left:654px"></div>
  <h3 class="footer-heading" style="left:742px">Quick contact</h3>
  <div class="field" style="left:743px;top:54px;width:121px;height:23px">Name</div>
  <div class="field" style="left:874px;top:54px;width:120px;height:23px">Email</div>
  <div class="field" style="left:743px;top:86px;width:251px;height:50px;padding-top:9px">Message</div>
  <div class="send">Send</div>
</footer>
<div class="copyright">Copyright 2014 Ferncast Construct Pty Ltd | ABN: 00 123 456 789 | Lic: 000000X</div>
</body>
</html>
```